Zielgruppe
Ich biete IT-Dienstleistungen von A-Z für Private Kunden sowie auch für KMU an.
Die Dienstleistungen wie Beratung, Support, Verkauf etc. biete ich vor Ort wie auch per Remote oder im Ladenlokal an. Das Ladenlokal gehört einem Geschäftskollegen und ich darf einen Arbeitsplatz ab und an nutzen für Kundentreffen.
Im Anschluss würde ich noch ein Flyerdesign benötigen und in Zukunft vielleicht weiteres Design Material.
Aufgabenstellung
2-seitige Visitenkarte, mindestens enthalten sein sollte darauf:
Logo, Firmenname, Webadresse, support@ Mailadresse, Postanschrift
Personenname, Funktion/Beruf, Telefonnummer, Mobilnummer
Falls platztechnisch machbar, wäre die zusätzliche Adresse vom Ladenlokal noch gut. Sonst stehen die Kunden an der falschen Adresse (Postanschrift).
Da dank Corona jeder einen QR-Code (er)kennt, wäre ich für einen optionalen QR-Code mit den wichtigsten Informationen von der Visitenkarte offen. Sollte es aber zu wenig Platz haben oder nicht sinnvoll platziert werden können, kann man es auch weg lassen.
beschreibende Stichworte: jung, dynamisch, seriös

```html
<!DOCTYPE html>
<html lang="de">
<head>
<meta charset="utf-8">
<title>kavestra – Visitenkarte</title>
<link rel="stylesheet" href="https://fonts.googleapis.com/css2?family=Comfortaa:wght@400;600;700&display=swap">
<style>
  :root {
    --stage: #e9e9eb;
    --paper: #ffffff;
    --teal: #1eabcc;
    --teal-deep: #1488a5;
    --teal-light: #a9d9e6;
    --ink: #404448;
    --grid-light: #ececee;
    --grid-deep: #1a9dbc;
  }
  * { box-sizing: border-box; margin: 0; padding: 0; }
  html, body { width: 1200px; height: 1200px; overflow: hidden; }
  body {
    background: var(--stage);
    font-family: "Comfortaa", sans-serif;
    color: var(--ink);
    position: relative;
  }
  .card {
    position: absolute;
    left: 300px;
    width: 600px;
    height: 388px;
    border-radius: 18px;
    overflow: hidden;
  }
  .card--front { top: 180px; background: var(--paper); }
  .card--back { top: 632px; background: var(--teal); }

  .texture {
    position: absolute;
    left: 0;
    width: 239px;
  }
  .card--front .texture { top: 0; height: 187px; background: var(--grid-light); }
  .card--back .texture { top: 200px; height: 188px; background: var(--grid-deep); }

  .brand { position: absolute; left: 272px; }
  .card--front .brand { top: 66px; }
  .card--back .brand { top: 66px; left: 266px; }
  .brand__name {
    display: flex;
    align-items: center;
    gap: 10px;
    font-size: 54px;
    font-weight: 700;
    line-height: 1;
    letter-spacing: -1px;
  }
  .brand__mark {
    width: 14px; height: 14px; border-radius: 50%;
    flex: none;
  }
  .card--front .brand__name { color: var(--teal); }
  .card--front .brand__mark { background: var(--ink); }
  .card--back .brand__name { color: #fff; }
  .card--back .brand__mark { background: var(--teal-deep); }
  .brand__tagline {
    margin-top: 8px;
    margin-left: 48px;
    font-size: 22px;
    font-weight: 400;
    white-space: nowrap;
  }
  .card--front .brand__tagline { color: var(--ink); }
  .card--back .brand__tagline { color: #fff; }

  .person {
    position: absolute;
    right: 363px;
    top: 224px;
    text-align: right;
  }
  .person__name { font-size: 23px; font-weight: 600; color: var(--teal); line-height: 1.1; }
  .person__role { font-size: 18px; color: var(--ink); margin-top: 2px; }

  .dots { position: absolute; display: flex; gap: 10px; }
  .dots span { width: 15px; height: 15px; border-radius: 50%; }
  .card--front .dots { left: 168px; top: 335px; }
  .card--front .dots span { background: var(--teal-deep); }
  .card--front .dots span:nth-child(2) { background: var(--teal); }
  .card--front .dots span:nth-child(3) { background: var(--teal-light); }
  .card--back .dots { left: 170px; top: 38px; }
  .card--back .dots span { background: #fff; }

  .contact {
    position: absolute;
    left: 300px;
    top: 192px;
    list-style: none;
    font-size: 16px;
    line-height: 20px;
    color: var(--ink);
  }
  .contact li { display: flex; align-items: flex-start; gap: 8px; }
  .contact li + li { margin-top: 0; }
  .contact .group-gap { margin-top: 20px; }
  .contact .icon { width: 14px; height: 14px; margin-top: 3px; flex: none; }
  .contact .label { color: var(--teal); }
  .contact .indent { padding-left: 22px; }

  .slogan {
    position: absolute;
    left: 266px;
    top: 170px;
    font-size: 22px;
    font-weight: 600;
    color: var(--teal-deep);
    word-spacing: 4px;
  }
  .web {
    position: absolute;
    left: 266px;
    top: 338px;
    font-size: 20px;
    font-weight: 600;
    color: #fff;
    letter-spacing: 0.5px;
  }
</style>
</head>
<body>

<section class="card card--front">
  <div class="texture" role="img" aria-label="Feines graues Punkteraster als Flächenmuster"></div>

  <div class="brand">
    <div class="brand__name">kavestra<span class="brand__mark"></span></div>
    <div class="brand__tagline">IT- &amp; Weblösungen</div>
  </div>

  <div class="person">
    <div class="person__name">Luka Renner</div>
    <div class="person__role">Informatiker</div>
  </div>

  <div class="dots"><span></span><span></span><span></span></div>

  <ul class="contact">
    <li>
      <svg class="icon" viewBox="0 0 14 14"><circle cx="7" cy="7" r="7" fill="var(--teal)"/><path d="M7 3.2a2.3 2.3 0 0 0-2.3 2.3C4.7 7.3 7 10.5 7 10.5s2.3-3.2 2.3-5A2.3 2.3 0 0 0 7 3.2z" fill="#fff"/><circle cx="7" cy="5.5" r="0.9" fill="var(--teal)"/></svg>
      <span class="label">Ladenlokal</span>
    </li>
    <li class="indent">Lindenweg 12, 8400 Talbach</li>
    <li class="indent label">Postanschrift</li>
    <li class="indent">Mühlegasse 7, 8400 Talbach</li>
    <li class="group-gap">
      <svg class="icon" viewBox="0 0 14 14"><circle cx="7" cy="7" r="7" fill="var(--teal)"/><path d="M4.6 3.6l1.3-.3.8 1.8-.9.7a5 5 0 0 0 2.3 2.3l.7-.9 1.8.8-.3 1.3c-3.3.2-6-2.5-5.7-5.7z" fill="#fff"/></svg>
      <span>052 555 01 73</span>
    </li>
    <li>
      <svg class="icon" viewBox="0 0 14 14"><circle cx="7" cy="7" r="7" fill="var(--teal)"/><rect x="4.8" y="3" width="4.4" height="8" rx="0.8" fill="#fff"/><rect x="5.6" y="4" width="2.8" height="5" fill="var(--teal)"/></svg>
      <span>052 555 01 72</span>
    </li>
    <li>
      <svg class="icon" viewBox="0 0 14 14"><circle cx="7" cy="7" r="7" fill="var(--teal)"/><rect x="3.5" y="4.5" width="7" height="5" rx="0.6" fill="#fff"/><path d="M3.8 4.8L7 7.3l3.2-2.5" fill="none" stroke="var(--teal)" stroke-width="0.8"/></svg>
      <span>info@kavestra.ch</span>
    </li>
  </ul>
</section>

<section class="card card--back">
  <div class="dots"><span></span><span></span><span></span></div>

  <div class="brand">
    <div class="brand__name">kavestra<span class="brand__mark"></span></div>
    <div class="brand__tagline">IT- &amp; Weblösungen</div>
  </div>

  <div class="slogan">jung · dynamisch · seriös</div>

  <div class="texture" role="img" aria-label="Punkteraster in dunklerem Türkis als Flächenmuster"></div>

  <div class="web">www.kavestra.ch</div>
</section>

</body>
</html>
```